Minimalist, Flat(Matte) design for a Beef Jerky packaging company. No bullshit company looking for a

Need a packaging design for a new Beef Jerky product(in English). The name of the company is 'Vellorn' and thus the packaging should reflect the bullish, tough, and simple nature of the beef jerky product. The finished product should communicate simplicity, minimalism, yet toughness and strength.

The logo should be simple, with a minimal number of colors , and should be either all white/cream, or have some red as well. Main colors should be white, cream, tinted red, and matte black. I think 4 colors max would be best. The closest example to an existing package style would be Kessip Noir clove cigarettes( image attached).

It will be on a matte black standing pouch package. See image for package type. Package dimensions:

Dimension: Width x Gusset x Height
INCH : 5.125" (W) x 3.125" (G) x 8.125" (H)
MILLIMETER : 130mm (W) x 80mm (G) x 205mm (H)

I don't have anything totally specific so artistic liberty is encouraged, provided the colors are kept to a minimum and looks consistent with the simple nature of the brand and the matte black packaging.

Also attached an existing beef jerky package with a similar style to what we're looking for.

Industry/Entity Type

It Company

Colors
f59195
ffffff

Requirements
Must have
• Low contrast, flat and minimalist design.
Should not have
• A complicated design with many colors. Gawdy/flashy design. Bright colors. High contrast.

```html
<!DOCTYPE html>
<html lang="en">
<head>
<meta charset="utf-8">
<title>Vellorn Peppered Beef Jerky – Pouch Front and Back</title>
<link rel="stylesheet" href="https://fonts.googleapis.com/css2?family=Montserrat:wght@400;500;600;800&display=swap">
<style>
  :root {
    --pouch-black: #000000;
    --zip-grey: #2a2a2a;
    --brand-red: #ef4a40;
    --zip-tint: #f58a80;
    --chili-red: #e8452f;
    --chili-dark: #b8321f;
    --ink-white: #ffffff;
    --page: #ffffff;
  }
  html, body {
    margin: 0;
    padding: 0;
    overflow: hidden;
    background: var(--page);
  }
  .canvas {
    position: relative;
    width: 1200px;
    height: 895px;
    overflow: hidden;
    background: var(--page);
    font-family: "Montserrat", sans-serif;
    color: var(--ink-white);
  }
  .pouch {
    position: absolute;
    top: 92px;
    width: 398px;
    height: 630px;
  }
  .pouch--front { left: 172px; }
  .pouch--back { left: 610px; }
  .pouch__shape {
    position: absolute;
    inset: 0;
    width: 398px;
    height: 630px;
  }
  .pouch__content {
    position: absolute;
    inset: 0;
  }

  /* brand band on front */
  .brand-band {
    position: absolute;
    left: 138px;
    top: 0;
    width: 124px;
    height: 191px;
    background: var(--brand-red);
  }
  .brand-band__zip {
    position: absolute;
    left: 0;
    top: 47px;
    width: 100%;
    height: 12px;
    background: var(--zip-tint);
    opacity: 0.75;
  }
  .brand-name {
    position: absolute;
    left: 0;
    width: 100%;
    text-align: center;
    font-weight: 600;
    letter-spacing: 0.02em;
    color: var(--ink-white);
    margin: 0;
    white-space: nowrap;
  }
  .brand-band .brand-name {
    top: 130px;
    font-size: 20px;
    line-height: 28px;
  }

  .line {
    position: absolute;
    left: 0;
    width: 100%;
    text-align: center;
    margin: 0;
    text-transform: uppercase;
  }
  .tagline {
    top: 243px;
    font-size: 24px;
    font-weight: 500;
    letter-spacing: 0.04em;
    line-height: 30px;
  }
  .flavour-frame {
    position: absolute;
    left: 49px;
    top: 316px;
    width: 297px;
    height: 77px;
    box-sizing: border-box;
    border: 2px solid var(--brand-red);
  }
  .flavour {
    position: absolute;
    left: 0;
    top: 11px;
    width: 100%;
    text-align: center;
    margin: 0;
    font-size: 46px;
    font-weight: 800;
    line-height: 52px;
    letter-spacing: 0.01em;
  }
  .chili {
    position: absolute;
    left: 147px;
    top: 388px;
    width: 102px;
    height: 9px;
    border-radius: 5px;
    background: linear-gradient(90deg, var(--chili-dark), var(--chili-red));
    box-shadow: 0 0 0 5px var(--pouch-black);
  }
  .product {
    top: 448px;
    font-size: 24px;
    font-weight: 500;
    letter-spacing: 0.04em;
    line-height: 30px;
  }
  .net-weight {
    position: absolute;
    margin: 0;
    font-size: 13px;
    font-weight: 500;
    white-space: nowrap;
    box-sizing: border-box;
  }
  .pouch--front .net-weight {
    top: 571px;
    left: 119px;
    width: 160px;
    line-height: 26px;
    text-align: center;
    border-left: 1px solid var(--ink-white);
    border-right: 1px solid var(--ink-white);
  }
  .pouch--back .net-weight {
    top: 561px;
    left: 0;
    width: 100%;
    text-align: center;
    line-height: 18px;
  }

  /* back panel */
  .open-here {
    position: absolute;
    left: 333px;
    top: 19px;
    margin: 0;
    font-size: 7px;
    letter-spacing: 0.05em;
    text-transform: uppercase;
  }
  .brand-tile {
    position: absolute;
    left: 159px;
    top: 316px;
    width: 79px;
    height: 92px;
    background: var(--brand-red);
  }
  .brand-tile .brand-name {
    top: 56px;
    font-size: 12px;
    line-height: 16px;
  }
  .description {
    position: absolute;
    left: 119px;
    top: 433px;
    width: 160px;
    margin: 0;
    text-align: center;
    font-size: 8.5px;
    font-weight: 400;
    line-height: 9.6px;
  }
</style>
</head>
<body>
<main class="canvas">

  <section class="pouch pouch--front" aria-label="Pouch front">
    <svg class="pouch__shape" viewBox="0 0 398 630" aria-hidden="true">
      <path d="M6 0 H392 Q398 0 398 6 V18 Q393 22 398 26 L387 630 H11 L0 26 Q5 22 0 18 V6 Q0 0 6 0 Z" fill="var(--pouch-black)"/>
      <rect x="11" y="48" width="378" height="4" fill="var(--zip-grey)"/>
      <rect x="11" y="56" width="378" height="1.5" fill="var(--zip-grey)"/>
    </svg>
    <div class="pouch__content">
      <div class="brand-band">
        <div class="brand-band__zip"></div>
        <p class="brand-name">VELLORN</p>
      </div>
      <p class="line tagline">Hand Crafted</p>
      <div class="flavour-frame">
        <h1 class="flavour">PEPPERED</h1>
      </div>
      <div class="chili" role="img" aria-label="Small red chili pepper illustration"></div>
      <p class="line product">Beef Jerky</p>
      <p class="net-weight">NET WT: 3 oz / 100g ℮</p>
    </div>
  </section>

  <section class="pouch pouch--back" aria-label="Pouch back">
    <svg class="pouch__shape" viewBox="0 0 398 630" aria-hidden="true">
      <path d="M6 0 H392 Q398 0 398 6 V18 Q393 22 398 26 L387 630 H11 L0 26 Q5 22 0 18 V6 Q0 0 6 0 Z" fill="var(--pouch-black)"/>
      <rect x="11" y="48" width="378" height="4" fill="var(--zip-grey)"/>
      <rect x="11" y="56" width="378" height="1.5" fill="var(--zip-grey)"/>
    </svg>
    <div class="pouch__content">
      <p class="open-here">Open here</p>
      <div class="brand-tile">
        <p class="brand-name">VELLORN</p>
      </div>
      <p class="description">Lorem ipsum dolor sit amet, consectetuer adipiscing elit, sed diam nonummy nibh euismod tincidunt ut laoreet dolore magna aliquam erat volutpat. Ut wisi enim ad minim veniam, quis nostrud exerci tation ullamcorper suscipit lobortis nisl ut aliquip ex ea commodo consequat.</p>
      <p class="net-weight">NET WT: 3 oz / 100g ℮</p>
    </div>
  </section>

</main>
</body>
</html>
```